Business Card Design

Lintel PR is a public relations consultancy service for the self build, home refurbishment and home improvement market.
It represents everything about 'home' so envisage logo featuring maybe roof pitch over the 'A' of Lintel. Colour/font undecided.

Industry/Entity Type

Home Improvement

Contact Information for Business Card

Fenella Stroudwick
fenella@lintelpr-example.co.uk
Telephone Direct: 0700 555 0142

```html
<!DOCTYPE html>
<html lang="en">
<head>
<meta charset="utf-8">
<title>Lintel PR — Business Card</title>
<link rel="stylesheet" href="https://fonts.googleapis.com/css2?family=Fira+Sans:wght@300&family=Arimo:wght@400&display=swap">
<style>
  :root {
    --card-bg: #e6e9ea;
    --card-bg-edge: #d9dddf;
    --wordmark-ink: #a53a1a;
    --wood-dark: #6a1d0c;
    --wood-mid: #a53a1a;
    --wood-light: #c0542b;
    --band-edge: #3d0f05;
    --name-white: #fbf3ee;
    --contact-ink: #2a1a14;
  }
  html, body {
    margin: 0;
    padding: 0;
    width: 1200px;
    height: 668px;
    overflow: hidden;
    background: var(--card-bg);
  }
  .card {
    position: relative;
    width: 1200px;
    height: 668px;
    background: radial-gradient(ellipse at 50% 40%, var(--card-bg) 60%, var(--card-bg-edge) 100%);
    overflow: hidden;
  }
  .brand-name {
    position: absolute;
    top: 150px;
    left: 0;
    width: 1200px;
    margin: 0;
    text-align: center;
    font-family: "Fira Sans", sans-serif;
    font-weight: 300;
    font-size: 112px;
    line-height: 1;
    color: var(--wordmark-ink);
  }
  .name-band {
    position: absolute;
    top: 428px;
    left: 0;
    width: 1200px;
    height: 140px;
    background:
      linear-gradient(180deg, rgba(0,0,0,0.35) 0, rgba(0,0,0,0) 14px, rgba(0,0,0,0) 126px, rgba(0,0,0,0.3) 140px),
      linear-gradient(90deg, var(--wood-dark) 0%, var(--wood-mid) 20%, var(--wood-light) 40%, var(--wood-mid) 60%, var(--wood-light) 80%, var(--wood-dark) 100%);
    border-top: 2px solid var(--band-edge);
    border-bottom: 2px solid var(--band-edge);
  }
  .person-name {
    position: absolute;
    top: 460px;
    left: 0;
    width: 1200px;
    margin: 0;
    text-align: center;
    font-family: "Fira Sans", sans-serif;
    font-weight: 300;
    font-size: 64px;
    line-height: 1.1;
    color: var(--name-white);
  }
  .contact-line {
    position: absolute;
    top: 600px;
    left: 214px;
    margin: 0;
    font-family: "Arimo", sans-serif;
    font-size: 22px;
    line-height: 1.2;
    color: var(--contact-ink);
    white-space: nowrap;
  }
  .contact-line .email {
    margin-left: 44px;
  }
</style>
</head>
<body>
  <main class="card">
    <h1 class="brand-name">Lintel PR</h1>
    <div class="name-band" role="img" aria-label="Polished reddish-brown wood plank band"></div>
    <p class="person-name">Fenella Stroudwick</p>
    <p class="contact-line">
      <span class="phone">Telephone Direct: 0700 555 0142</span>
      <span class="email">fenella@lintelpr-example.co.uk</span>
    </p>
  </main>
</body>
</html>
```